Brisk Hounds Dog Behaviour, Training and Natural Healthcare Business Card Design

I am an experienced and qualified dog behavioural trainer and natural animal healthcare consultant offering a range of services to help pet dog owners with the "whole dog".
COLOURS: A soft light blue in the background - can be fading out or split, red should also feature
LOGO: Dog, healing hands, silhouette, shadow
SERVICES: Behaviour Consults, Training, Complex Skills Coaching Walking Coaching, Diet & Nutrition, Environmental Enrichment, Lifestyle and Lifestage Adaptations, Massage, Natural Health Options
BY LINE: Happy Dogs, Happy Owners
VALUES: Promoting communication and connection between dogs and their owners.
FOCUS: Nutritional guidance and environmental adaptation are often needed to complete the package and increase the success rate of training and behaviour modification.

Target Market(s)

Everyone who has a dog who they wish to improve their relationship with

Industry/Entity Type

Communication

Contact Information for Business Card

Brisk Hounds, Renata Walcott, 0472 680351, briskhounds7@mailnest.example, www.briskhounds7.example, Qualified Dog Behavioural Trainer and Natural Animal Healthcare Consultant

Font styles to use
Sans Serif
Script

Colors
85cae6
ec2027

Requirements
Must have
• A clear indication that it is a dog services business. A raised feature
Should not have
• Pawprints, cartoons

```html
<!DOCTYPE html>
<html lang="en">
<head>
<meta charset="utf-8">
<title>Brisk Hounds – Business Card</title>
<link rel="stylesheet" href="https://fonts.googleapis.com/css2?family=EB+Garamond:wght@400;700&display=swap">
<style>
  :root {
    --card-blue: #67cbe3;
    --ink: #1f0f22;
  }
  * { margin: 0; padding: 0; box-sizing: border-box; }
  html, body {
    width: 1200px;
    height: 741px;
    overflow: hidden;
    background: var(--card-blue);
  }
  .card {
    position: relative;
    width: 1200px;
    height: 741px;
    background: var(--card-blue);
    color: var(--ink);
    font-family: "EB Garamond", Garamond, serif;
  }
  .mascot-area {
    position: absolute;
    left: 476px;
    top: 108px;
    width: 250px;
    height: 190px;
    border-radius: 18px;
    background: var(--ink);
  }
  .identity {
    position: absolute;
    left: 0;
    top: 370px;
    width: 100%;
    text-align: center;
  }
  .business-name {
    font-size: 40px;
    font-weight: 700;
    line-height: 48px;
  }
  .person-name {
    font-size: 29px;
    font-weight: 700;
    line-height: 46px;
  }
  .role {
    font-size: 34px;
    font-weight: 400;
    line-height: 48px;
    margin-top: 4px;
  }
  .contact-row {
    position: absolute;
    top: 653px;
    left: 81px;
    right: 76px;
    display: flex;
    justify-content: space-between;
    font-size: 28px;
    font-weight: 700;
    line-height: 40px;
  }
</style>
</head>
<body>
  <main class="card">
    <div class="mascot-area" role="img" aria-label="Dark silhouette of a seated dog facing right"></div>

    <section class="identity">
      <h1 class="business-name">Brisk Hounds</h1>
      <h2 class="person-name">Renata Walcott</h2>
      <p class="role">Qualified Dog Behavioural Trainer<br>and Natural Animal Healthcare Consultant</p>
    </section>

    <footer class="contact-row">
      <span class="contact-phone">0472 680351</span>
      <span class="contact-email">briskhounds7@mailnest.example</span>
      <span class="contact-web">www.briskhounds7.example</span>
    </footer>
  </main>
</body>
</html>
```